Business Card Design

We need a new business card design for our company, Pebble Forge.

Our website: www.brightcove7.ca

We are open to all ideas, from professional to very creative.
Updates

Design update requests:

1. We would like to see some examples with "BrightCove7" instead of "Pebble Forge" as the company name.
2. Would like to see "Software | Web | Branding" included on the card somewhere as well.

Thanks.

We are really trying to express the nature of our business through our business card.  "Pebble" can be misconstrued for the health industry, so use of "BrightCove7" and the "Software | Web | Branding" slogan are key to understanding our business.

We have uploaded a new PSD which includes a monitor, tablet, and phone screen.  This represents the flexibility of web applications and is another tool we would like to see used on business cards.

We will be eliminating designs today and will await updated designs with these new specs.

Thank-you.

Industry/Entity Type

Business

Requirements
Must have
• Content:
First M. Last
Managing Partner
e. email@brightcove7.ca
p. 555.555.5555

```html
<!DOCTYPE html>
<html lang="en">
<head>
<meta charset="utf-8">
<title>Quillmere7 Business Card</title>
<link rel="stylesheet" href="https://fonts.googleapis.com/css2?family=Arimo:wght@400;700&display=swap">
<style>
  :root {
    --backdrop: #eeeeee;
    --card: #ffffff;
    --brand-blue: #0a95d9;
    --sky-blue: #7fcdf0;
    --deep-blue: #1a5f8a;
    --ink: #4a4a4a;
    --ink-soft: #555555;
    --rule: #cfcfcf;
    --tile-light: #e6f4fb;
  }
  * { margin: 0; padding: 0; box-sizing: border-box; }
  html, body {
    width: 1200px;
    height: 1087px;
    overflow: hidden;
    background: var(--backdrop);
    font-family: "Arimo", Arial, sans-serif;
  }
  .card {
    position: absolute;
    left: 100px;
    top: 254px;
    width: 1000px;
    height: 578px;
    background: var(--card);
    box-shadow: 3px 4px 6px rgba(0,0,0,0.25);
    overflow: hidden;
  }
  .pattern-field {
    position: absolute;
    left: 622px;
    top: 216px;
    width: 378px;
    height: 331px;
    background: linear-gradient(90deg, rgba(230,244,251,0) 0%, var(--tile-light) 55%, #d9eef9 100%);
  }
  .brand-mark {
    position: absolute;
    left: 250px;
    top: 110px;
    width: 130px;
    height: 130px;
    background: var(--brand-blue);
  }
  .brand-name {
    position: absolute;
    left: 424px;
    top: 116px;
    font-size: 64px;
    font-weight: 700;
    color: var(--ink);
    letter-spacing: -2px;
    line-height: 1;
  }
  .tagline {
    position: absolute;
    left: 425px;
    top: 192px;
    font-size: 27px;
    line-height: 1;
    color: var(--brand-blue);
  }
  .tagline .web { color: var(--sky-blue); }
  .tagline .branding { color: var(--deep-blue); }
  .tagline .sep { color: var(--ink-soft); font-size: 19px; padding: 0 6px; vertical-align: 3px; }
  .devices {
    position: absolute;
    left: 184px;
    top: 302px;
    width: 224px;
    height: 116px;
    background: linear-gradient(135deg, #3a3a3a 0%, #6d6d6d 100%);
    border-radius: 4px;
  }
  .divider {
    position: absolute;
    left: 426px;
    top: 265px;
    width: 2px;
    height: 215px;
    background: var(--rule);
  }
  .person-name {
    position: absolute;
    left: 439px;
    top: 274px;
    font-size: 31px;
    font-weight: 700;
    color: var(--brand-blue);
    letter-spacing: 1.5px;
    line-height: 1;
  }
  .person-role {
    position: absolute;
    left: 439px;
    top: 323px;
    font-size: 21px;
    color: var(--ink-soft);
    line-height: 1;
  }
  .contact-line {
    position: absolute;
    left: 437px;
    display: flex;
    align-items: center;
    font-size: 22px;
    color: var(--ink-soft);
    line-height: 1;
  }
  .contact-line svg { width: 24px; height: 24px; margin-right: 7px; flex: none; }
  .contact-line.email { top: 382px; }
  .contact-line.phone { top: 423px; }
  .base-band {
    position: absolute;
    left: 0;
    bottom: 0;
    width: 100%;
    height: 31px;
    background: var(--brand-blue);
  }
</style>
</head>
<body>
  <main class="card">
    <div class="pattern-field" role="img" aria-label="Faint field of light blue tiles fading in from the right"></div>

    <div class="brand-mark" aria-hidden="true"></div>
    <div class="brand-name">Quillmere7</div>
    <div class="tagline">Software<span class="sep">|</span><span class="web">Web</span><span class="sep">|</span><span class="branding">Branding</span></div>

    <div class="devices" role="img" aria-label="Illustration of a desktop monitor, tablet and phone"></div>

    <div class="divider"></div>

    <h1 class="person-name">First M. Last</h1>
    <p class="person-role">Managing Partner</p>
    <p class="contact-line email">
      <svg viewBox="0 0 28 28" aria-hidden="true">
        <circle cx="14" cy="14" r="14" fill="var(--brand-blue)"/>
        <rect x="7" y="9" width="14" height="10" rx="1.5" fill="none" stroke="#fff" stroke-width="2"/>
        <polyline points="7.5,10 14,15 20.5,10" fill="none" stroke="#fff" stroke-width="2"/>
      </svg>
      email@quillmere7.ca
    </p>
    <p class="contact-line phone">
      <svg viewBox="0 0 28 28" aria-hidden="true">
        <circle cx="14" cy="14" r="14" fill="var(--brand-blue)"/>
        <path d="M10 7.5c1 0 1.6.4 2 1.5l.8 2.2c.3.8 0 1.4-.6 1.9l-.8.6c.8 1.7 2 2.9 3.7 3.7l.6-.8c.5-.6 1.1-.9 1.9-.6l2.2.8c1.1.4 1.5 1 1.5 2 0 1.6-1.4 3-3 2.7C12.7 20.6 7.4 15.3 6.5 10.7 6.2 9 8.4 7.5 10 7.5z" fill="#fff"/>
      </svg>
      555.555.5555
    </p>

    <div class="base-band"></div>
  </main>
</body>
</html>
```